IT Services company requires a services website design with integrated blog

We at Brambleway Code Haulage primarily provide application migration consultancy (e.g. moving applications from Paneview QR to Paneview 5) and application virtualization (e.g. Dunmore Box-K) consultancy.This process is commonly known as 'packaging' but doesnt involve cardboard boxes ;) (however, I am happy to use that visual analogy if you want to use any box graphics) We also provide application compatibility testing, software auditing and application portfolio management.

We are looking for a complete redesign of our current horrible diy attempt at a website at www.brambleway-example.com. We have had created a rebranded logo (attached files and fonts) and a rebranded business card (also attached) We would like the website to match the same/similar colors and styling as these.

I want to redisgn the website so that the main focus of this website is to show our subject matter expertise with a blog and should take up most of the websites real estate and focus on the home screen. Then if the customer wants, they can use our services to help them in their own application migration/deployment projects by browsing our details in links/buttons somewhere

In any of the designs, please do not include my Velharo or Dunmore partnerships.  Thank you

Target Market(s)

Application packagers / engineers looking for technical articles

Application migration project managers

Industry/Entity Type

Real Estate

Requirements
Must have
• This site is primarily a blog site. The blog should have buttons to share each article on social media site. It should be easy for me to create or edit new blog articles (have technical skills but not creative ones). Each article should also allow for comments (do not require approval but should allow for admin removal) but do not add like/vote buttons because i do not expect large enough traffic and could be determental.

There should be a contact page to host contact information and an email box that goes to enquiries@brambleway-example.com

The other pages should include About us and Services (placeholder text to be used as current site text needs overhauling but original text can be used in the design just remember when placing that the text may shorten or increase etc.)

All text has to be easily editable (no over use of text in images where possible)
Nice to have
• An email notification of new comments to articles sent to webadmin@brambleway-example.com

Newsletter subscription
Should not have
• Do not include vote/like buttons or website counters. Initial traffic is not going to be large enough to warrant these features and may reflect badly on the site.

No logon features. Site content and commenting should be open access

No opinion polls

No why choose us section from current website

Do not include partner information in new site (Velharo and Dunmore)

DO NOT JUST REPLICATE EXISTING WEBSITE FEATURES, PLEASE REFER TO THIS BRIEF. THIS SITE NEEDS TO PRIMARILY BE A BLOG

```html
<!DOCTYPE html>
<html lang="en">
<head>
<meta charset="utf-8">
<title>Brambleway Code Haulage – Application Packaging Blog</title>
<link rel="stylesheet" href="https://fonts.googleapis.com/css2?family=Questrial&family=PT+Sans:wght@400;700&display=swap">
<style>
:root{
  --taupe:#6c665a;
  --blue:#5a78e2;
  --blue-soft:#7d95ea;
  --blue-ink:#1f5b9a;
  --grey-text:#666158;
  --white:#ffffff;
}
*{margin:0;padding:0;box-sizing:border-box}
html,body{width:1159px;height:1200px;overflow:hidden;background:var(--white)}
body{position:relative;font-family:"Questrial",sans-serif;color:var(--grey-text)}
.abs{position:absolute}
a{color:inherit;text-decoration:none}

.topbar{left:0;top:0;width:1159px;height:25px;background:var(--taupe);color:var(--white);font-size:10.5px}
.topbar .mail{left:166px;top:6px}
.topbar .social{right:165px;top:7px;display:flex;gap:10px;font-size:9px;align-items:center}
.topbar .social span+span{border-left:1px dotted #bdb7aa;padding-left:8px}

.masthead{left:0;top:25px;width:1159px;height:107px;background:linear-gradient(#fafafa,#e9e9ec)}
.brand{left:166px;top:22px;display:flex;align-items:center;gap:10px}
.brand .dot{width:34px;height:34px;border-radius:50%;background:var(--blue)}
.brand .name{font-size:21px;line-height:22px;color:var(--grey-text)}
.search{left:836px;top:14px;width:158px;height:20px;border:1px solid #d4d4d6;background:var(--white);font-size:7.5px;padding:6px 0 0 19px;color:#555}
.search svg{position:absolute;right:5px;top:4px}
.nav{right:165px;top:66px;display:flex;font-size:10.5px;color:#55504a}
.nav span{padding:0 12px}
.nav span:last-child{padding-right:0}
.nav i{font-style:normal;color:#777}

.hero{left:0;top:132px;width:1159px;height:347px;background:linear-gradient(135deg,#5c7ae4 0%,#5474de 60%,#6884e6 100%)}
.hero .brandline{left:166px;top:32px;display:flex;align-items:center;gap:14px;color:var(--white)}
.hero .brandline .name{font-size:20px;line-height:21px;border-left:1px solid #fff;padding-left:10px}
.hero .brandline .tag{font-family:"PT Sans",sans-serif;font-weight:700;font-size:25px;margin-left:6px}
.hero h1{left:164px;top:92px;font-family:"PT Sans",sans-serif;font-weight:700;font-size:50px;line-height:60px;color:var(--white);letter-spacing:.5px}
.hero p{left:168px;top:154px;width:330px;font-size:9.8px;line-height:12px;color:var(--white);font-weight:700}
.btn{display:inline-block;border:1px solid #9c9c9c;border-radius:5px;background:linear-gradient(#ffffff,#d7d7d9);color:var(--blue-ink);text-align:center}
.hero .btn{left:273px;top:248px;width:139px;height:37px;font-family:"PT Sans",sans-serif;font-weight:700;font-size:19px;line-height:35px}
.hero .visual{left:538px;top:5px;width:456px;height:342px;border-radius:170px 0 0 0;background:radial-gradient(circle at 30% 45%,#5aa6e8 0%,#2e6fc4 35%,rgba(84,116,222,0) 62%),linear-gradient(90deg,rgba(84,116,222,0) 55%,#6d86b3 70%,#5d7ab0 90%,rgba(84,116,222,0) 100%)}

.welcome{left:0;top:479px;width:1159px;height:121px;background:linear-gradient(#e6e6e8,#f8f8f9)}
.welcome h2{left:179px;top:18px;font-family:"PT Sans",sans-serif;font-weight:700;font-size:23px;color:var(--blue-ink);letter-spacing:.5px}
.welcome p{left:179px;top:53px;width:805px;font-size:10.6px;line-height:12px;color:var(--blue)}
.welcome .more{left:900px;top:92px;font-size:12px;color:var(--blue-ink)}
.rule{left:165px;top:611px;width:829px;border-top:1px dotted #aaa}

.card{color:var(--white)}
.card.blue{background:var(--blue-soft)}
.card.dark{background:var(--taupe);box-shadow:0 6px 10px rgba(0,0,0,.25)}
.card h3{font-family:"PT Sans",sans-serif;font-weight:700;font-size:19px;line-height:22px;padding:0 16px 9px;border-bottom:1px solid rgba(255,255,255,.45)}
.card .date{font-size:9.5px;font-style:italic;padding:8px 16px 0}
.card .body{font-size:12px;line-height:14px;padding:18px 16px 0}
.card .tools{position:absolute;right:16px;top:8px;display:flex;gap:6px}
.card .btn{position:absolute;right:10px;bottom:9px;width:76px;height:20px;font-size:9.5px;line-height:18px}
.c1{left:165px;top:643px;width:236px;height:246px;padding-top:28px}
.c2{left:401px;top:627px;width:361px;height:262px;padding-top:44px}
.c3{left:762px;top:643px;width:232px;height:246px;padding-top:28px}
.c2 h3{padding-bottom:20px}

.details h2,.news h2{font-family:"PT Sans",sans-serif;font-weight:700;font-size:26px;color:var(--grey-text)}
.details{left:165px;top:925px;width:435px;height:220px}
.details p{margin-top:22px;font-size:11px;line-height:13px}
.details .btn{position:absolute;left:0;top:194px;width:76px;height:20px;font-size:9.5px;line-height:18px}
.vrule{left:651px;top:936px;height:186px;border-left:1px dotted #999}
.news{left:697px;top:925px;width:300px;height:220px}
.item{display:flex;gap:10px;margin-top:12px}
.news .item:first-of-type{margin-top:20px}
.day{width:35px;height:31px;flex:none;background:var(--blue-soft);color:var(--white);text-align:center;font-size:11px;line-height:12px;padding-top:3px;border:1px solid #c8d2f4}
.item .txt{width:215px}
.item b{display:block;font-weight:400;font-size:11.5px;color:var(--blue-ink);text-decoration:underline}
.item small{display:block;font-size:7.6px;line-height:10px;margin-top:3px;color:#444}
.news .btn{position:absolute;left:3px;top:195px;width:76px;height:20px;font-size:9.5px;line-height:18px}

.footer{left:0;top:1153px;width:1159px;height:47px;background:var(--taupe);color:var(--white);font-size:10.5px;font-style:italic}
.footer .links{left:166px;top:17px;display:flex}
.footer .links span{padding:0 9px}
.footer .links span:first-child{padding-left:0}
.footer .copy{right:165px;top:18px;font-size:9.5px}
</style>
</head>
<body>

<header>
  <div class="abs topbar">
    <span class="abs mail">enquiries@brambleway-example.com</span>
    <div class="abs social">
      <span>Friendloop</span><span>Chirpline</span><span>RSS</span>
      <span><svg width="14" height="10" viewBox="0 0 14 10" style="vertical-align:-1px"><rect x="0.5" y="0.5" width="13" height="9" fill="none" stroke="#fff"/><path d="M0.5 0.5 7 5.5 13.5 0.5" fill="none" stroke="#fff"/></svg> Email</span>
    </div>
  </div>
  <div class="abs masthead">
    <div class="abs brand"><span class="dot"></span><span class="name">Brambleway<br>Code Haulage</span></div>
    <div class="abs search">SEARCH
      <svg width="11" height="11" viewBox="0 0 11 11"><circle cx="4.5" cy="4.5" r="3.3" fill="none" stroke="#555" stroke-width="1.4"/><path d="M7 7 10 10" stroke="#555" stroke-width="1.6"/></svg>
    </div>
    <nav class="abs nav">
      <span>Home</span><i>/</i><span>Blog</span><i>/</i><span>About Us</span><i>/</i><span>Our Services</span><i>/</i><span>Contact</span>
    </nav>
  </div>
</header>

<section class="abs hero">
  <div class="abs brandline"><span class="name">Brambleway<br>Code Haulage</span><span class="tag">TECHNOLOGIES</span></div>
  <h1 class="abs">PROFESSIONALS</h1>
  <p class="abs">Lorem ipsum dolor sit amet, consectetuer adipiscing elit, sed diam nonummy nibh euismod tincidunt ut laoreet dolore to aliquam erat volutpat. Ut wisi enim ad minim veniam, quis nostrud exerci tation ullamcorper suscipit lobortis nisl ut aliquip ex ea commodo conat.</p>
  <a class="abs btn">READ MORE</a>
  <div class="abs visual" role="img" aria-label="Photo of a smiling consultant in a blue shirt holding a laptop in front of a glowing world globe"></div>
</section>

<section class="abs welcome">
  <h2 class="abs">WELCOME</h2>
  <p class="abs">Our blog shares hands-on articles on application packaging, migration and virtualization.&nbsp; Read guides on moving applications from Paneview QR to Paneview 5, sequencing with Dunmore Box-K, compatibility testing, software auditing and application portfolio management.<br>New technical articles are posted regularly for packagers, engineers and migration project managers.<br>need help with a project? contact us today for more information</p>
  <a class="abs more">READ MORE...</a>
</section>
<div class="abs rule"></div>

<svg width="0" height="0" style="position:absolute">
  <defs>
    <g id="tool-set">
      <rect x="0" y="1" width="11" height="13" fill="#fff" stroke="#c33" stroke-width="1"/>
      <rect x="19" y="5" width="13" height="7" rx="1" fill="#eee" stroke="#555"/>
      <rect x="22" y="1" width="7" height="4" fill="#fff" stroke="#555"/>
      <rect x="39" y="4" width="13" height="9" fill="#f7f2d8" stroke="#888"/>
      <path d="M39 4 45.5 9 52 4" fill="none" stroke="#888"/>
    </g>
  </defs>
</svg>

<article class="abs card blue c1">
  <svg class="tools" width="52" height="15"><use href="#tool-set"/></svg>
  <h3>Packaging for Paneview 5</h3>
  <div class="date">Tuesday, 19 June 2012 16:47</div>
  <div class="body">A step-by-step look at moving legacy applications from Paneview QR to Paneview 5, with the checks we run before every package goes live...</div>
  <a class="btn">READ MORE</a>
</article>

<article class="abs card dark c2">
  <svg class="tools" width="52" height="15"><use href="#tool-set"/></svg>
  <h3>Sequencing Tips for Box-K</h3>
  <div class="date">Saturday, 09 June 2012 13:58</div>
  <div class="body">Application virtualization is only as good as the sequence behind it. In this article we walk through clean build machines, exclusion lists and testing of each Box-K package...<br>&nbsp;We also cover common pitfalls with shared runtimes, drivers and services, and how to spot them early in your project...</div>
  <a class="btn">READ MORE</a>
</article>

<article class="abs card blue c3">
  <svg class="tools" width="52" height="15"><use href="#tool-set"/></svg>
  <h3>Testing App Compatibility</h3>
  <div class="date">Thursday, 31 May 2012 08:27</div>
  <div class="body">A practical checklist for compatibility testing before a migration, from inventory and triage to sign-off. Find out how we keep large portfolios on track...</div>
  <a class="btn">READ MORE</a>
</article>

<section class="abs details">
  <h2>Details</h2>
  <p>Lorem ipsum dolor sit amet, consectetuer adipiscing elit, sed diam nonummy nibh euismod tincidunt ut laoreet dolore magna aliquam erat volutpat. Ut wisi enim ad minim veniam, quis nostrud exerci tation ullamcorper suscipit lobortis nisl ut aliquip ex ea commodo consequat. Duis autem vel eum iriure dolor in hendrerit in vulputate velit esse molestie consequat, vel illum dolore eu feugiat nulla facilisis at vero eros et accumsan et iusto odio dignissim qui blandit praesent luptatum zzril delenit augue duis dolore te feugait nulla facilisi.</p>
  <a class="btn">READ MORE</a>
</section>
<div class="abs vrule"></div>

<section class="abs news">
  <h2>Latest Articles</h2>
  <div class="item"><div class="day">24<br>MAR</div><div class="txt"><b>Lorem ipsum dolor sit amet</b><small>sed diam nonummy nibh euismod tincidunt ut laoreet dolore magna....</small></div></div>
  <div class="item"><div class="day">24<br>July</div><div class="txt"><b>Lorem ipsum dolor sit amet</b><small>sed diam nonummy nibh euismod tincidunt ut laoreet dolore magna...</small></div></div>
  <div class="item"><div class="day">23<br>JAN</div><div class="txt"><b>Lorem ipsum dolor sit amet</b><small>sed diam nonummy nibh euismod tincidunt ut<br>laoreet dolore magna...</small></div></div>
  <a class="btn">READ MORE</a>
</section>

<footer class="abs footer">
  <div class="abs links"><span>Home</span><span>/</span><span>Blog</span><span>/</span><span>About Us</span><span>/</span><span>Our Services</span><span>/</span><span>Contact</span></div>
  <div class="abs copy">Copyright © 2013 Brambleway Code Haulage ltd. All Rights Reserved.</div>
</footer>

</body>
</html>
```